Wildlife photographer Website

The website is to be a "resume" of pictures and awards won by Nora. Lean heavy to outdoor wildlife.
She will post articles and have ability to interact with fans.

I will add some of her pictures tonight,

Target Market(s)

Terra Quarterly .....anyone looking to hire a wildlife photographer.

Industry/Entity Type

Professional Photography

Contact Information for Business Card

Nora Falkett
4817 Maple Hollow Lane
Columbia MD 21078
443-581-2094
Nora@FernOwlPix.com

Coding

Coded - Design and coding required

Number of Pages Required

5+ page

Requirements
Must have
• New Logo
Nice to have
• Nature, and eye catching graphics

```html
<!DOCTYPE html>
<html lang="en">
<head>
<meta charset="utf-8">
<title>Nora Falkett — Blog</title>
<link href="https://fonts.googleapis.com/css2?family=Montserrat:wght@600;700&display=swap" rel="stylesheet">
<style>
  :root {
    --sidebar-bg: #000000;
    --text: #ffffff;
    --accent: #f5a833;
    --dot-muted: #7d8590;
    --tile-geese-a: #2e2c2b;
    --tile-geese-b: #4a4236;
    --tile-plover-a: #3d362f;
    --tile-plover-b: #5a4b3c;
    --tile-cardinal-a: #464a58;
    --tile-cardinal-b: #5b4a3a;
    --tile-gull-a: #1a2636;
    --tile-gull-b: #3a4452;
  }
  * { margin: 0; padding: 0; box-sizing: border-box; }
  html, body { width: 1200px; height: 771px; overflow: hidden; background: #000; }
  body {
    position: relative;
    font-family: "Montserrat", Arial, sans-serif;
    color: var(--text);
  }
  .sidebar {
    position: absolute; left: 0; top: 0; width: 271px; height: 771px;
    background: var(--sidebar-bg);
  }
  .site-name {
    position: absolute; left: 43px; top: 40px;
    font-size: 28px; font-weight: 700; letter-spacing: 0.2px;
  }
  .main-nav { position: absolute; left: 43px; top: 137px; list-style: none; }
  .main-nav li { height: 32.6px; font-size: 12px; font-weight: 700; line-height: 18px; }
  .main-nav a { color: var(--text); text-decoration: none; }
  .main-nav .current a { color: var(--accent); }
  .social-links {
    position: absolute; left: 43px; top: 694px;
    display: flex; gap: 9px; list-style: none;
  }
  .social-links a {
    display: flex; align-items: center; gap: 4px;
    font-size: 10px; font-weight: 700; color: var(--text); text-decoration: none;
  }
  .social-links a::before {
    content: ""; width: 10px; height: 10px; border: 1.5px solid var(--text); border-radius: 50%;
  }
  .post-tile { position: absolute; width: 465px; height: 386px; overflow: hidden; }
  .tile-1 { left: 271px; top: 0; }
  .tile-2 { left: 735px; top: 0; }
  .tile-3 { left: 271px; top: 385px; }
  .tile-4 { left: 735px; top: 385px; }
  .tile-photo { position: absolute; inset: 0; }
  .tile-1 .tile-photo { background: radial-gradient(ellipse at 50% 40%, var(--tile-geese-b), var(--tile-geese-a) 70%); }
  .tile-2 .tile-photo { background: radial-gradient(ellipse at 35% 30%, var(--tile-plover-b), var(--tile-plover-a) 75%); }
  .tile-3 .tile-photo { background: radial-gradient(ellipse at 40% 60%, var(--tile-cardinal-b), var(--tile-cardinal-a) 65%); }
  .tile-4 .tile-photo { background: radial-gradient(ellipse at 75% 60%, var(--tile-gull-b), var(--tile-gull-a) 65%); }
  .post-title, .post-excerpt, .read-more { position: absolute; left: 70px; }
  .tile-2 .post-title, .tile-2 .post-excerpt, .tile-2 .read-more,
  .tile-4 .post-title, .tile-4 .post-excerpt, .tile-4 .read-more { left: 79px; }
  .post-title { font-size: 21.5px; font-weight: 700; line-height: 36px; white-space: nowrap; }
  .post-excerpt { font-size: 12px; font-weight: 700; white-space: nowrap; }
  .tile-1 .post-excerpt { line-height: 36px; }
  .tile-2 .post-excerpt, .tile-3 .post-excerpt, .tile-4 .post-excerpt { line-height: 27.5px; }
  .read-more { font-size: 12.5px; font-weight: 700; color: var(--accent); text-decoration: none; line-height: 18px; }
  .tile-1 .post-title { top: 48px; }
  .tile-1 .post-excerpt { top: 159px; }
  .tile-1 .read-more { top: 303px; }
  .tile-2 .post-title { top: 94px; }
  .tile-2 .post-excerpt { top: 173px; }
  .tile-2 .read-more { top: 288px; }
  .tile-3 .post-title { top: 70px; }
  .tile-3 .post-excerpt { top: 185px; }
  .tile-3 .read-more { top: 300px; }
  .tile-4 .post-title { top: 97px; }
  .tile-4 .post-excerpt { top: 140px; }
  .tile-4 .read-more { top: 254px; }
  .page-dots { position: absolute; left: 1145px; top: 558px; list-style: none; }
  .page-dots li { width: 8px; height: 8px; border-radius: 50%; background: var(--dot-muted); margin-bottom: 12.3px; }
  .page-dots .active { background: var(--text); }
  .page-dots .current { background: var(--accent); }
  .scroll-arrows { position: absolute; left: 1143px; top: 692px; }
</style>
</head>
<body>
  <aside class="sidebar">
    <div class="site-name">Nora Falkett</div>
    <ul class="main-nav">
      <li><a href="#">Home</a></li>
      <li><a href="#">Works</a></li>
      <li><a href="#">About Me</a></li>
      <li><a href="#">Contact</a></li>
      <li class="current"><a href="#">Blog</a></li>
      <li><a href="#">Search</a></li>
    </ul>
    <ul class="social-links">
      <li><a href="#">Nest</a></li>
      <li><a href="#">Perch</a></li>
      <li><a href="#">Wing</a></li>
      <li><a href="#">Trill</a></li>
    </ul>
  </aside>

  <article class="post-tile tile-1">
    <div class="tile-photo" role="img" aria-label="Photo of snow geese in flight against a dark sky"></div>
    <h2 class="post-title">Vivamus nunc massa,<br>hendrerit semper ex sed/</h2>
    <p class="post-excerpt">Vivamus nunc massa, hendrerit semper ex sed,<br>mollis tincidunt ex. Phasellus magna dolor, finibus<br>ac leo in, sodales tempor nisl. Pellentesque sed</p>
    <a class="read-more" href="#">Read more</a>
  </article>

  <article class="post-tile tile-2">
    <div class="tile-photo" role="img" aria-label="Photo of a small shorebird standing on wet sand"></div>
    <h2 class="post-title">Massa nunc massa.</h2>
    <p class="post-excerpt">Vivamus nunc massa, hendrerit semper ex sed,<br>mollis tincidunt ex. Phasellus magna dolor, finibus<br>ac leo in, sodales tempor nisl.</p>
    <a class="read-more" href="#">Read more</a>
  </article>

  <article class="post-tile tile-3">
    <div class="tile-photo" role="img" aria-label="Photo of a female cardinal in the snow"></div>
    <h2 class="post-title">Hendrerit semper ex sed,<br>mollis Nucea.</h2>
    <p class="post-excerpt">Mollis tincidunt ex. Phasellus magna dolor, finibus<br>ac leo in, sodales tempor nisl. Pellentesque sed<br>rutrum tortor. Morbi faucibus porttitor sem.</p>
    <a class="read-more" href="#">Read more</a>
  </article>

  <article class="post-tile tile-4">
    <div class="tile-photo" role="img" aria-label="Photo of a calling gull against a dark blue background"></div>
    <h2 class="post-title">Massa nunc massa.</h2>
    <p class="post-excerpt">Vivamus nunc massa, hendrerit semper ex sed,<br>mollis tincidunt ex. Phasellus magna dolor, finibus<br>ac leo in, sodales tempor nisl.</p>
    <a class="read-more" href="#">Read more</a>
  </article>

  <ul class="page-dots">
    <li></li>
    <li></li>
    <li class="active"></li>
    <li class="current"></li>
  </ul>

  <svg class="scroll-arrows" width="14" height="36" viewBox="0 0 14 36" aria-hidden="true">
    <polyline points="2,8 7,3 12,8" fill="none" stroke="#ffffff" stroke-width="1.8" stroke-linecap="round" stroke-linejoin="round"/>
    <polyline points="2,28 7,33 12,28" fill="none" stroke="#ffffff" stroke-width="1.8" stroke-linecap="round" stroke-linejoin="round"/>
  </svg>
</body>
</html>
```